Flyer for spiritual retreat (yoga, meditation, reiki, raw food)

I would like a flyer to promote my upcoming retreat and a matching Facebook banner.

The name of the retreat is "Blossomreach Within" and the tagline is "retreat into you"

The activities in the retreat include daily meditation, ecstatic dance, spiritual development workshops on intuition, energy healing etc and a reiki session is included.

I would like a flyer designed to promote this, something that is editable as I will be running this multiple times and will need to adjust the flyer to add the dates etc each time.

edit: add that here will be fully catered raw food and juices, and that the retreat price includes all accomodation, meals and workshops.

Please contact me if you need further info. Please also visit my website www.marniekovac-studio.com and www.friendhub-sample.com/tuvelanook to see my current events and promotions.

Thank you,

Marnie

Reason: Hi all, thank you all for your submissions. Apologies as I am traveling and do not have much access to internet and will review your submissions and provide feedback as soon as possible. Kind regards, Marnie.

Target Market(s)

People who like meditation, yoga, fans of ronan feldspar and mervin okoro, those interested in personal and spiritual development.

Industry/Entity Type

Health And Wellness

Requirements
Must have
• Please put the included reiki session as as added bonus. Something like "BONUS 30 minute reiki healing session" in a little star/banner/something that stands out.
• Please emphasise the "light" part of Blossomreach as I am going for a play on words between in the light and enlightenment.
• Please include placeholder text for place, location, time
• Placeholder for price
• My name (see attached file - can change colour to suit) and website (www.marniekovac-studio.com)
Nice to have
• I prefer rounded designs, curves rather than block designs.
Should not have
• Tuvela Nook logo

```html
<!DOCTYPE html>
<html lang="en">
<head>
<meta charset="utf-8">
<title>Blossomreach Within – retreat into you</title>
<link rel="stylesheet" href="https://fonts.googleapis.com/css2?family=Lobster+Two:ital,wght@0,700;1,700&family=Questrial&display=swap">
<style>
  :root {
    --night: #000000;
    --sun-gold: #f6a21e;
    --sun-deep: #e07b0c;
    --sky-top: #6e5a3c;
    --sky-mid: #c9822a;
    --glow: #ffc24a;
    --light: #fff6d8;
    --white: #ffffff;
    --ink: #1a1208;
    --band: #f6a82c;
    --muted: #d9c6a4;
  }
  * { margin: 0; padding: 0; box-sizing: border-box; }
  html, body { width: 849px; height: 1200px; overflow: hidden; background: var(--night); }
  .flyer {
    position: relative;
    width: 849px;
    height: 1200px;
    background: var(--night);
    font-family: "Questrial", sans-serif;
    color: var(--white);
    overflow: hidden;
  }
  .sunset-photo {
    position: absolute;
    left: 0; top: 0;
    width: 849px; height: 600px;
    background:
      radial-gradient(ellipse 170px 110px at 355px 505px, var(--glow) 0%, rgba(246,162,30,0.7) 40%, rgba(246,162,30,0) 100%),
      linear-gradient(180deg, var(--sky-top) 0%, #8a6a3a 25%, var(--sky-mid) 50%, #7a4a10 72%, var(--night) 100%);
  }
  .title {
    position: absolute;
    left: 0; width: 849px;
    top: 58px;
    text-align: center;
    font-family: "Lobster Two", cursive;
    font-weight: 700;
    font-style: italic;
    font-size: 120px;
    line-height: 116px;
    color: var(--white);
    text-shadow: 0 4px 8px rgba(0,0,0,0.45);
  }
  .title .line { display: block; }
  .title .light-word {
    color: var(--light);
    text-shadow: 0 0 18px rgba(255,214,120,0.95), 0 0 40px rgba(255,190,70,0.7), 0 4px 8px rgba(0,0,0,0.35);
  }
  .title .within { color: var(--sun-gold); }
  .tagline-row {
    position: absolute;
    left: 0; width: 849px;
    top: 300px;
    display: flex;
    justify-content: center;
    align-items: center;
    gap: 16px;
  }
  .ornament {
    width: 80px; height: 10px;
    border-radius: 5px;
  }
  .ornament.left { background: var(--white); }
  .ornament.right { background: var(--sun-gold); }
  .tagline {
    font-family: "Lobster Two", cursive;
    font-weight: 700;
    font-size: 50px;
    background: linear-gradient(90deg, var(--white) 0%, #ffe0a8 40%, var(--sun-gold) 100%);
    -webkit-background-clip: text;
    background-clip: text;
    color: transparent;
    filter: drop-shadow(0 3px 4px rgba(0,0,0,0.5));
  }
  .activities {
    position: absolute;
    left: 0; width: 849px;
    top: 540px;
    list-style: none;
    text-align: center;
    font-size: 31px;
    line-height: 49.5px;
    letter-spacing: 1.5px;
  }
  .activities li::before {
    content: "";
    display: inline-block;
    width: 16px; height: 16px;
    margin-right: 7px;
    border: 2px solid var(--white);
    border-radius: 50%;
    background: radial-gradient(circle, var(--white) 0 3.5px, transparent 4px);
    vertical-align: 1px;
  }
  .catering-box {
    position: absolute;
    left: 94px; top: 810px;
    width: 660px; height: 168px;
    background: var(--band);
    border-radius: 12px;
    color: var(--ink);
    font-size: 29px;
    line-height: 39px;
    text-align: center;
    padding-top: 25px;
    letter-spacing: 0.8px;
  }
  .bonus-badge {
    position: absolute;
    left: 154px; top: 1000px;
    width: 540px; height: 50px;
    border: 2px solid var(--sun-gold);
    border-radius: 25px;
    display: flex;
    align-items: center;
    justify-content: center;
    gap: 12px;
    font-size: 21px;
    letter-spacing: 0.8px;
    color: var(--white);
  }
  .bonus-badge .bonus-label {
    background: var(--sun-gold);
    color: var(--ink);
    border-radius: 14px;
    padding: 3px 12px;
    font-size: 18px;
    letter-spacing: 1.5px;
  }
  .event-details {
    position: absolute;
    left: 0; width: 849px;
    top: 1068px;
    text-align: center;
    font-size: 20px;
    line-height: 34px;
    letter-spacing: 1px;
    color: var(--muted);
  }
  .event-details .price { color: var(--sun-gold); font-size: 22px; }
  .footer-band {
    position: absolute;
    left: 0; top: 1166px;
    width: 849px; height: 34px;
    background: var(--band);
    color: var(--ink);
    font-size: 17px;
    display: flex;
    justify-content: space-between;
    align-items: center;
    padding: 0 41px 0 42px;
  }
</style>
</head>
<body>
<main class="flyer">
  <div class="sunset-photo" role="img" aria-label="Photograph of a golden sunset behind silhouetted trees and tall grass, fading into darkness"></div>

  <h1 class="title">
    <span class="line">Blossom<span class="light-word">reach</span></span>
    <span class="line within">Within</span>
  </h1>

  <div class="tagline-row">
    <span class="ornament left" role="img" aria-label="Decorative flourish"></span>
    <p class="tagline">retreat into you</p>
    <span class="ornament right" role="img" aria-label="Decorative flourish"></span>
  </div>

  <ul class="activities">
    <li>daily meditation</li>
    <li>estatic dance</li>
    <li>spiritual development workshops on intuition</li>
    <li>energy healing etc</li>
    <li>and a reiki session</li>
  </ul>

  <div class="catering-box">
    <p>fully catered raw food and juices,<br>
    and that the retreat price includes all<br>
    accommodation, meals and workshops</p>
  </div>

  <div class="bonus-badge">
    <span class="bonus-label">BONUS</span>
    <span>30 minute reiki healing session</span>
  </div>

  <div class="event-details">
    <p>date &middot; time &middot; place &middot; location</p>
    <p class="price">price: £000</p>
  </div>

  <footer class="footer-band">
    <span class="website">www.marniekovac-studio.com</span>
    <span class="social">www.friendhub-sample.com/tuvelanook</span>
  </footer>
</main>
</body>
</html>
```